KT Sentry 'Welcome' Envelope

I am looking for a 'Welcome' envelope design for new customers who sign up for our Alarm Services. In this envelope we will send confidential documents that the customer will need. I want it to stand out, yet look classy.

```html
<!DOCTYPE html>
<html lang="en">
<head>
<meta charset="utf-8">
<title>KT Sentry Welcome Envelope</title>
<link href="https://fonts.googleapis.com/css2?family=Poppins:wght@300;400;600&display=swap" rel="stylesheet">
<style>
:root{
  --stage:#b3b3b3;
  --sheet:#030b11;
  --env-dark:#071722;
  --env-mid:#0c3348;
  --env-teal:#115170;
  --flap:#0c2c3a;
  --band:#0e3a52;
  --green:#3ec43a;
  --text:#e8eef2;
  --icon:#2a73b0;
  --line:#6d8796;
}
*{margin:0;padding:0;box-sizing:border-box}
html,body{width:741px;height:1200px;overflow:hidden}
body{background:var(--stage);font-family:'Poppins',sans-serif;color:var(--text);position:relative}
.envelope{position:absolute;width:530px;height:231px;overflow:hidden;
  background:linear-gradient(90deg,var(--env-dark) 0%,var(--env-mid) 45%,var(--env-teal) 62%,var(--env-mid) 80%,var(--env-dark) 100%)}
.aperture-art{position:absolute;border-radius:50%;
  background:radial-gradient(circle,rgba(40,120,160,.35) 0%,rgba(20,80,110,.25) 55%,rgba(10,40,60,0) 72%)}
.lens-art{position:absolute;width:92px;height:92px;border-radius:50%;
  background:radial-gradient(circle at 45% 42%,#7fe0ff 0%,#1f8fd0 22%,#0b4f86 42%,#1b2a36 60%,#9aa9b3 66%,#2b3a44 74%,#0a1c28 100%)}
.band{position:absolute;left:0;right:0;background:var(--band);opacity:.8}
.stripes{position:absolute;left:0;right:0;height:22px;
  background:repeating-linear-gradient(180deg,rgba(170,190,200,.35) 0 1px,transparent 1px 3px)}
.watermark{position:absolute;width:176px;height:102px;background:rgba(170,185,195,.16);
  clip-path:polygon(14% 0,86% 0,100% 50%,86% 100%,14% 100%,0 50%)}
.watermark .mark{position:absolute;left:0;right:0;top:36px;text-align:center;font-size:22px;font-weight:600;color:rgba(10,30,45,.55)}
.watermark .note{position:absolute;left:0;right:0;text-align:center;font-size:5px;color:rgba(200,215,225,.35)}
.brand{position:absolute;font-weight:600;color:var(--green);font-size:21px;line-height:1;letter-spacing:.5px}
.brand::before{content:"";display:inline-block;width:9px;height:9px;background:var(--icon);margin-right:6px;vertical-align:2px}
.contact{position:absolute;left:19px;font-size:9.4px;font-weight:300;line-height:14.5px;display:flex;gap:7px}
.contact svg{width:10px;height:10px;flex:none;margin-top:2px;fill:var(--icon)}
.window{position:absolute;left:22px;top:152px;width:174px;height:67px;background:#fff;border-radius:8px;box-shadow:0 1px 3px rgba(0,0,0,.5)}
.notice{position:absolute;font-weight:300;white-space:nowrap;display:flex;align-items:center}
.notice::before{content:"";width:.42em;height:.42em;background:var(--green);transform:rotate(45deg);margin-right:.3em}
.flap-strip{position:absolute;left:0;right:0;top:0;height:51px;background:var(--flap);
  clip-path:polygon(0 0,100% 0,89% 100%,11% 100%)}
.sheet{position:absolute;left:28px;top:556px;width:684px;height:607px;background:var(--sheet)}
.outline{position:absolute;inset:0;width:100%;height:100%}
.flipped{transform:rotate(180deg)}
</style>
</head>
<body>

<!-- Front -->
<section class="envelope" style="left:113px;top:37px;" aria-label="Envelope front">
  <div class="aperture-art" role="img" aria-label="Camera aperture graphic" style="left:20px;top:-110px;width:480px;height:480px"></div>
  <div class="band" style="top:177px;height:24px"></div>
  <div class="stripes" style="top:199px"></div>
  <div class="watermark" style="left:350px;top:59px"><span class="note" style="top:-10px">Security Products Dealer</span><div class="mark">KT Sentry</div><span class="note" style="top:88px">24 Hour Protection</span></div>
  <div class="lens-art" role="img" aria-label="Camera lens" style="left:224px;top:74px"></div>
  <div class="brand" style="left:19px;top:30px">KT Sentry</div>
  <div class="contact" style="top:57px"><svg viewBox="0 0 10 10"><path d="M5 0a3.5 3.5 0 0 0-3.5 3.5C1.5 6 5 10 5 10s3.5-4 3.5-6.5A3.5 3.5 0 0 0 5 0zm0 5a1.4 1.4 0 1 1 0-2.8A1.4 1.4 0 0 1 5 5z"/></svg><span>PO Box 450219<br>Linden, ID 83400</span></div>
  <div class="contact" style="top:116px"><svg viewBox="0 0 10 10"><rect width="10" height="10" rx="2"/><path d="M3 2.5l1 1.5-.6.7a4 4 0 0 0 1.9 1.9L6 6l1.5 1-.6 1C4.5 8 2 5.5 2 3.1z" fill="#071722"/></svg><span>555 . 214 . 0938</span></div>
  <div class="contact" style="top:133px"><svg viewBox="0 0 10 10"><path d="M5 1a4 4 0 1 1-3.7 2.5L0 3V0l1 1.2A4 4 0 0 1 5 1zm0 1.2A2.8 2.8 0 1 0 7.8 5 2.8 2.8 0 0 0 5 2.2zM4.5 3h1v2l1.3 1-.6.7L4.5 5.5z"/></svg><span>24 HOUR PROTECTION</span></div>
  <div class="window"></div>
  <div class="notice" style="left:303px;top:176px;font-size:21px">OPEN IMMEDIATELY</div>
</section>

<!-- Back -->
<section class="envelope" style="left:113px;top:303px;" aria-label="Envelope back">
  <div class="aperture-art" role="img" aria-label="Camera aperture graphic" style="left:18px;top:-110px;width:480px;height:480px"></div>
  <div class="flap-strip"></div>
  <div class="band" style="top:169px;height:22px"></div>
  <div class="watermark" style="left:347px;top:62px"><span class="note" style="top:-10px">Security Products Dealer</span><div class="mark">KT Sentry</div><span class="note" style="top:88px">24 Hour Protection</span></div>
  <div class="lens-art" role="img" aria-label="Camera lens" style="left:212px;top:75px"></div>
  <div class="brand" style="left:196px;top:171px">KT Sentry</div>
  <div class="notice" style="left:201px;top:193px;font-size:10px">OPEN IMMEDIATELY</div>
</section>

<!-- Dieline -->
<section class="sheet" aria-label="Envelope dieline">
  <svg class="outline" viewBox="0 0 684 607">
    <polygon points="113,46 569,46 606,96 77,96" fill="#0c2c3a" stroke="#5f7d8c" stroke-width=".6"/>
    <path d="M77,98 L35,111 Q26,114 26,124 L26,296 Q26,306 35,309 L77,321" fill="none" stroke="#5f7d8c" stroke-width=".6"/>
    <path d="M606,98 L648,111 Q657,114 657,124 L657,296 Q657,306 648,309 L606,321" fill="none" stroke="#5f7d8c" stroke-width=".6"/>
  </svg>
  <section class="envelope" style="left:77px;top:96px;" aria-label="Front on dieline">
    <div class="aperture-art" role="img" aria-label="Camera aperture graphic" style="left:20px;top:-110px;width:480px;height:480px"></div>
    <div class="band" style="top:177px;height:24px"></div>
    <div class="stripes" style="top:199px"></div>
    <div class="watermark" style="left:350px;top:59px"><span class="note" style="top:-10px">Security Products Dealer</span><div class="mark">KT Sentry</div><span class="note" style="top:88px">24 Hour Protection</span></div>
    <div class="lens-art" role="img" aria-label="Camera lens" style="left:224px;top:74px"></div>
    <div class="brand" style="left:19px;top:30px">KT Sentry</div>
    <div class="contact" style="top:57px"><svg viewBox="0 0 10 10"><path d="M5 0a3.5 3.5 0 0 0-3.5 3.5C1.5 6 5 10 5 10s3.5-4 3.5-6.5A3.5 3.5 0 0 0 5 0zm0 5a1.4 1.4 0 1 1 0-2.8A1.4 1.4 0 0 1 5 5z"/></svg><span>PO Box 450219<br>Linden, ID 83400</span></div>
    <div class="contact" style="top:116px"><svg viewBox="0 0 10 10"><rect width="10" height="10" rx="2"/><path d="M3 2.5l1 1.5-.6.7a4 4 0 0 0 1.9 1.9L6 6l1.5 1-.6 1C4.5 8 2 5.5 2 3.1z" fill="#071722"/></svg><span>555 . 214 . 0938</span></div>
    <div class="contact" style="top:133px"><svg viewBox="0 0 10 10"><path d="M5 1a4 4 0 1 1-3.7 2.5L0 3V0l1 1.2A4 4 0 0 1 5 1zm0 1.2A2.8 2.8 0 1 0 7.8 5 2.8 2.8 0 0 0 5 2.2zM4.5 3h1v2l1.3 1-.6.7L4.5 5.5z"/></svg><span>24 HOUR PROTECTION</span></div>
    <div class="window"></div>
    <div class="notice" style="left:303px;top:176px;font-size:21px">OPEN IMMEDIATELY</div>
  </section>
  <section class="envelope flipped" style="left:77px;top:327px;" aria-label="Back on dieline">
    <div class="aperture-art" role="img" aria-label="Camera aperture graphic" style="left:18px;top:-110px;width:480px;height:480px"></div>
    <div class="band" style="top:169px;height:22px"></div>
    <div class="watermark" style="left:347px;top:62px"><span class="note" style="top:-10px">Security Products Dealer</span><div class="mark">KT Sentry</div><span class="note" style="top:88px">24 Hour Protection</span></div>
    <div class="lens-art" role="img" aria-label="Camera lens" style="left:212px;top:75px"></div>
    <div class="brand" style="left:196px;top:171px">KT Sentry</div>
    <div class="notice" style="left:201px;top:193px;font-size:10px">OPEN IMMEDIATELY</div>
  </section>
</section>

</body>
</html>
```